Valtrix Energy Information Site Redesign

Re-vamp current site at valtrixenergy.example to include new logo, verbiage updates as needed, redesign, etc. Company overview and additional information on current Valtrix url.

```html
<!DOCTYPE html>
<html lang="en">
<head>
<meta charset="utf-8">
<title>Valtrix Energy Information</title>
<link rel="stylesheet" href="https://fonts.googleapis.com/css2?family=Poppins:wght@400;500;600;700&family=Open+Sans:ital,wght@0,400;0,600;0,700;1,400&display=swap">
<style>
:root{
  --blue:#1b6fc0;
  --blue-dark:#0f4f94;
  --navy:#0d2f5a;
  --orange:#f7941d;
  --ink:#222;
  --text:#555;
  --panel:#efefef;
  --white:#fff;
}
*{margin:0;padding:0;box-sizing:border-box}
html,body{width:1200px;height:3822px;overflow:hidden}
body{position:relative;font-family:"Open Sans",sans-serif;color:var(--text);background:var(--white)}
.abs{position:absolute}
.heading{font-family:"Poppins",sans-serif}
.btn{position:absolute;background:var(--orange);color:var(--white);font:500 17px "Poppins",sans-serif;display:flex;align-items:center;justify-content:center;border-radius:3px;text-transform:uppercase}

/* header */
.brand{position:absolute;left:76px;top:20px;display:flex;align-items:center;gap:12px}
.brand-dot{width:54px;height:54px;border-radius:50%;background:var(--orange)}
.brand-name{font:600 26px "Poppins",sans-serif;color:var(--blue)}
.call{position:absolute;left:888px;top:26px;display:flex;gap:14px;align-items:center}
.call-label{font-size:15px;color:#333}
.call-number{font:700 27px "Poppins",sans-serif;color:var(--orange);line-height:1}

.nav{position:absolute;left:0;top:107px;width:1200px;height:61px;background:var(--blue)}
.nav a{position:absolute;top:0;height:61px;line-height:61px;color:var(--white);font-size:15px;text-decoration:none}
.nav .active{background:var(--orange);padding:0 26px;font-weight:600}

.hero{position:absolute;left:0;top:168px;width:1200px;height:515px;background:linear-gradient(180deg,#1c3550 0%,#243d58 45%,#1a2c40 100%)}
.hero-title{position:absolute;top:300px;width:1200px;text-align:center;font:700 60px "Poppins",sans-serif;color:var(--white)}
.hero-sub{position:absolute;top:386px;left:230px;width:740px;text-align:center;font-size:20px;color:var(--white);line-height:1.5}

.services{position:absolute;top:683px;left:0;width:1200px;height:275px;display:flex}
.service{width:400px;height:275px;background:var(--blue);color:var(--white);text-align:center;padding:74px 60px 0}
.service.alt{background:var(--orange)}
.service h3{font:600 20px "Poppins",sans-serif;text-transform:uppercase;margin-bottom:8px}
.service p{font-size:14px;line-height:1.65}
.service .more{display:inline-block;margin-top:10px;font-size:14px;color:var(--orange);text-decoration:underline}
.service.alt .more{color:#7a3f00}
.service-icon{position:absolute;top:619px;width:112px;height:112px;border-radius:50%;background:var(--white);border:6px solid var(--white);box-shadow:0 0 0 3px rgba(0,0,0,.08);display:flex;align-items:center;justify-content:center}
.service-icon .ring{width:94px;height:94px;border-radius:50%;background:var(--blue);display:flex;align-items:center;justify-content:center}
.service-icon.alt .ring{background:var(--orange)}

.welcome h2{position:absolute;left:76px;top:1016px;font:500 38px "Poppins",sans-serif;color:var(--blue)}
.accent{color:var(--orange)}
.welcome p{position:absolute;left:76px;width:640px;font-size:13.5px;line-height:1.75}

.testimonial{position:absolute;top:1368px;left:0;width:1200px;height:319px;background:linear-gradient(90deg,#1a5aa0,#2a78c4 50%,#1a5aa0)}
.testimonial h2{position:absolute;top:75px;width:1200px;text-align:center;font:500 38px "Poppins",sans-serif;color:var(--white)}
.quote{position:absolute;left:321px;top:148px;width:800px;font:italic 14px/1.9 "Open Sans",sans-serif;color:var(--white)}
.cite{position:absolute;right:86px;top:252px;font-size:13px;color:var(--orange)}

.feature h3{position:absolute;top:2040px;font:600 21px "Poppins",sans-serif;color:var(--blue);text-transform:uppercase;letter-spacing:.5px}
.feature p{position:absolute;top:2082px;width:370px;font-size:13.5px;line-height:1.75}

.clients{position:absolute;top:2281px;left:0;width:1200px;height:565px;background:linear-gradient(180deg,#123b6e,#1b5494 50%,#123b6e)}
.clients h2{position:absolute;top:58px;width:1200px;text-align:center;font:500 25px "Poppins",sans-serif;color:var(--white)}
.clients h4{position:absolute;top:103px;width:1200px;text-align:center;font:600 20px "Poppins",sans-serif;color:var(--orange);text-transform:uppercase}
.client-col{position:absolute;top:175px;list-style:none}
.client-col li{height:33px;font-size:13px;color:var(--white);display:flex;align-items:center;gap:10px}
.client-col li::before{content:"";width:9px;height:9px;border-radius:50%;background:var(--orange)}
.client-col li.current{color:var(--orange)}

.blog-title{position:absolute;top:2896px;width:1200px;text-align:center;font:500 40px "Poppins",sans-serif;color:var(--blue)}
.blog-card{position:absolute;left:173px;top:2986px;width:884px;height:344px;background:var(--panel)}
.date{position:absolute;left:0;top:0;width:89px;height:90px;background:var(--orange);color:var(--white);text-align:center;font-family:"Poppins",sans-serif}
.date b{display:block;font-size:36px;line-height:1.3;padding-top:4px}
.date span{font-size:13px;font-weight:600}
.blog-card h3{position:absolute;left:352px;top:44px;width:480px;font:700 19px/1.6 "Poppins",sans-serif;color:var(--ink)}
.blog-card p{position:absolute;left:352px;top:113px;width:500px;font-size:13px;line-height:1.75}

.footer{position:absolute;top:3458px;left:0;width:1200px;height:308px;background:var(--blue);color:var(--white)}
.footer h5{position:absolute;top:40px;font:600 18px "Poppins",sans-serif;text-transform:uppercase}
.links{position:absolute;left:433px;top:80px;list-style:none}
.links li{height:27px;font-size:13px;display:flex;align-items:center;gap:10px}
.links li::before{content:"";width:6px;height:6px;border-radius:50%;background:var(--orange)}
.contact{position:absolute;left:790px;font-size:13.5px;line-height:1.65;display:flex;gap:16px}
.social{position:absolute;top:3672px;width:40px;height:40px;border-radius:50%;background:var(--blue-dark);border:2px solid rgba(255,255,255,.5)}
.copyright{position:absolute;top:3766px;left:0;width:1200px;height:56px;background:var(--blue-dark);color:var(--white);font-size:13px;display:flex;align-items:center;justify-content:center}
</style>
</head>
<body>

<header>
  <div class="brand"><span class="brand-dot"></span><span class="brand-name">Valtrix Energy</span></div>
  <div class="call">
    <svg width="36" height="36" viewBox="0 0 24 24"><path fill="#f7941d" d="M6.6 10.8c1.4 2.8 3.8 5.1 6.6 6.6l2.2-2.2c.3-.3.7-.4 1-.2 1.1.4 2.3.6 3.6.6.6 0 1 .4 1 1V20c0 .6-.4 1-1 1C10.6 21 3 13.4 3 4c0-.6.4-1 1-1h3.5c.6 0 1 .4 1 1 0 1.3.2 2.5.6 3.6.1.3 0 .7-.2 1z"/></svg>
    <div><div class="call-label">Call Us On :</div><div class="call-number">800-555-0142</div></div>
  </div>
</header>

<nav class="nav">
  <a class="active" style="left:76px">Home</a>
  <a style="left:204px">What We Do</a>
  <a style="left:321px">Exchange Solutions</a>
  <a style="left:497px">Data Management</a>
  <a style="left:657px">Owner Relations Services</a>
  <a style="left:874px">About Valtrix</a>
  <a style="left:998px">Blog</a>
  <a style="left:1050px">Contact Us</a>
</nav>

<section class="hero" role="img" aria-label="Control room with analysts at screens in front of a world map display"></section>
<h1 class="hero-title">VALTRIX ENERGY</h1>
<p class="hero-sub">Valtrix provides the technology to efficiently transfer information electronically and access, integrate and manage data.</p>

<section class="services">
  <div class="service"><h3>Well Data Exchange</h3><p>Our platform for partner reports, logs, surveys and countless other documents, allows you to outsource</p><span class="more">Read More... »</span></div>
  <div class="service alt"><h3>Partner Data Exchange</h3><p>Our exchange solutions enable companies to automatically exchange data which can be integrated into their</p><span class="more">Read More... »</span></div>
  <div class="service"><h3>E-Ticket Exchange</h3><p>Valtrix automates the transfer of field tickets between logistics service providers and oil &amp; gas operating companies</p><span class="more">Read More... »</span></div>
</section>
<div class="service-icon" style="left:144px"><div class="ring"><svg width="44" height="40" viewBox="0 0 44 40"><rect x="3" y="3" width="38" height="26" rx="2" fill="none" stroke="#fff" stroke-width="3"/><path d="M16 36h12M22 29v7M10 12h24M10 19h18" stroke="#fff" stroke-width="3"/></svg></div></div>
<div class="service-icon alt" style="left:544px"><div class="ring"><svg width="46" height="46" viewBox="0 0 46 46"><rect x="3" y="3" width="16" height="16" fill="none" stroke="#fff" stroke-width="3"/><rect x="27" y="27" width="16" height="16" fill="none" stroke="#fff" stroke-width="3"/><path d="M19 11h16v12M27 35H11V23" fill="none" stroke="#fff" stroke-width="3"/></svg></div></div>
<div class="service-icon" style="left:944px"><div class="ring"><svg width="48" height="36" viewBox="0 0 48 36"><rect x="3" y="6" width="42" height="24" rx="3" fill="none" stroke="#fff" stroke-width="3"/><path d="M14 18h20M28 12l6 6-6 6M20 12l-6 6 6 6" fill="none" stroke="#fff" stroke-width="3"/></svg></div></div>

<section class="welcome">
  <h2 class="heading">WELCOME TO <span class="accent">VALTRIX ENERGY</span></h2>
  <p style="top:1086px">Valtrix Energy Information has been providing electronic exchange solutions for the energy industry for over 20 years.</p>
  <p style="top:1138px">Valtrix utilizes proven data integration techniques to provide customers with cost effective methods to efficiently access, transform and distribute their data. Our customer list includes over 95% of the Fortune 500 energy companies</p>
  <div class="btn" style="left:76px;top:1251px;width:171px;height:51px">Learn More</div>
  <div class="abs" style="left:765px;top:958px;width:435px;height:410px;background:linear-gradient(135deg,#f4f6f8,#d9e2ea 55%,#b9c9d8)" role="img" aria-label="Hands holding a tablet showing connected data icons"></div>
</section>

<section class="testimonial" role="img" aria-label="Blurred blue data centre backdrop">
  <h2>WHAT OUR <span class="accent">CLIENT SAY</span></h2>
  <div class="abs" style="left:199px;top:135px;width:102px;height:102px;border-radius:50%;background:#c98a6a;border:4px solid #fff" role="img" aria-label="Client portrait"></div>
  <p class="quote">" Without Valtrix I would have to hire 2-3 more employees to keep up with the demand of keying lines in. The customer support staff has been GREAT to work with. It's hard to imagine life without Valtrix. They have certainly made my life easier!"</p>
  <span class="cite">— Keystone Trust Company</span>
  <span class="abs" style="left:1147px;top:134px;width:14px;height:14px;border-radius:50%;background:#fff"></span>
  <span class="abs" style="left:1147px;top:165px;width:14px;height:14px;border-radius:50%;border:2px solid #fff"></span>
</section>

<section class="feature">
  <div class="abs" style="left:214px;top:1750px;width:377px;height:271px;background:radial-gradient(circle at 50% 60%,#2f8fd0,#0c2f55 75%)" role="img" aria-label="Hand holding a glowing globe of data connections"></div>
  <div class="abs" style="left:609px;top:1750px;width:377px;height:271px;background:linear-gradient(135deg,#3a5670,#1e3346 60%,#4b6b86)" role="img" aria-label="Cityscape overlaid with digital network graphics"></div>
  <h3 style="left:214px">Data <span class="accent">Management</span></h3>
  <p style="left:214px">Our data management solutions make it easier for your company to track and manage production and other mission critical business data.</p>
  <div class="btn" style="left:214px;top:2171px;width:171px;height:51px">Learn More</div>
  <h3 style="left:609px">Owner <span class="accent">Relations Services</span></h3>
  <p style="left:609px">With over 85 companies, Valtrix operates the largest network of internet owner portals in the industry.</p>
  <div class="btn" style="left:609px;top:2171px;width:171px;height:51px">Learn More</div>
</section>

<section class="clients" role="img" aria-label="Server room corridor in deep blue light">
  <h2>WANT TO SEE WHAT VALTRIX ENERGY CAN DO FOR YOUR COMPANY ?</h2>
  <h4>Visit some of our client-branded customer &amp; owner relations website</h4>
  <ul class="client-col" style="left:140px"><li class="current">Amberline</li><li>Arvo Resources</li><li>Aldenrock</li><li>Ashgrove</li><li>Axton</li><li>Auren</li><li>Brix Holloway</li><li>BK</li><li>Calderon</li><li>Cedarfall</li></ul>
  <ul class="client-col" style="left:390px"><li>Coldbrook</li><li>Corvane</li><li>Crestal/CRL</li><li>Covemark Resources</li><li>Cobalt Ridge</li><li>Dunmore</li><li>Driftwood</li><li>Elmtex</li><li>Ember Energy</li><li>Endara</li></ul>
  <ul class="client-col" style="left:606px"><li>EQL Resources</li><li>Exmo</li><li>Fenwick Resources</li><li>Fieldstone Energy</li><li>GRV Hartsdale</li><li>Kessler-Forde</li><li>Le Marlow</li><li>Lyle Energy</li><li>Merra-Tolan</li><li>Meridale Oil</li></ul>
  <ul class="client-col" style="left:884px"><li>Millbourne</li><li>Northgate</li><li>Norland Energy</li><li>PRK Energy</li><li>Petrowren</li><li>Pinehaven</li><li>Prairieway</li><li>Plateau Marketing</li><li>QRT Resources</li><li>Rosalind</li></ul>
  <svg class="abs" style="left:22px;top:282px" width="18" height="34" viewBox="0 0 18 34"><path d="M15 3L3 17l12 14" fill="none" stroke="rgba(255,255,255,.6)" stroke-width="3"/></svg>
  <svg class="abs" style="left:1160px;top:282px" width="18" height="34" viewBox="0 0 18 34"><path d="M3 3l12 14L3 31" fill="none" stroke="rgba(255,255,255,.6)" stroke-width="3"/></svg>
</section>

<section class="blog">
  <h2 class="blog-title"><span class="accent">LATEST</span> BLOG</h2>
  <article class="blog-card">
    <div class="abs" style="left:0;top:0;width:314px;height:344px;background:linear-gradient(180deg,#7d8a96,#3e4a55 60%,#26303a)" role="img" aria-label="Oil pumpjack at dusk with headline overlay"></div>
    <div class="date"><b>04</b><span>JULY</span></div>
    <h3>Harlan Oil &amp; Gas Joins Valtrix Production Exchange</h3>
    <p>We are pleased to announce that Harlan Oil &amp; Gas LLC has joined the Valtrix Energy Production Exchange. By participating in Valtrix Energy's leading reciprocal data sharing network, Harlan joins hundreds of operating companies who use Valtrix to share monthly and daily production volumes with their working interest owners and other operating companies.</p>
    <div class="btn" style="left:352px;top:253px;width:173px;height:48px">Learn More</div>
  </article>
  <svg class="abs" style="left:553px;top:3353px" width="96" height="42" viewBox="0 0 96 42"><circle cx="21" cy="21" r="19" fill="#fff" stroke="#ccc" stroke-width="2"/><circle cx="72" cy="21" r="19" fill="#fff" stroke="#ccc" stroke-width="2"/><path d="M24 14l-7 7 7 7M69 14l7 7-7 7" fill="none" stroke="#666" stroke-width="2"/></svg>
</section>

<footer class="footer">
  <div class="abs" style="left:203px;top:48px;width:74px;height:74px;border-radius:50%;background:var(--white)"></div>
  <div class="abs" style="left:95px;top:140px;width:290px;text-align:center;font:600 30px 'Poppins',sans-serif">Valtrix Energy</div>
  <h5 style="left:433px">Quick <span class="accent">Links</span></h5>
  <ul class="links"><li>What We Do</li><li>Exchange Solutions</li><li>Data Management</li><li>Owner Relations Services</li><li>About Valtrix</li><li>Blog</li><li>Contact Us</li></ul>
  <h5 style="left:790px">Contact <span class="accent">Info</span></h5>
  <div class="contact" style="top:80px"><svg width="16" height="22" viewBox="0 0 16 22"><path d="M8 0a8 8 0 0 0-8 8c0 6 8 14 8 14s8-8 8-14a8 8 0 0 0-8-8zm0 11a3 3 0 1 1 0-6 3 3 0 0 1 0 6z" fill="#f7941d"/></svg><span>450 Meridian Ave.<br>Suite 200<br>Springdale, TX 75001</span></div>
  <div class="contact" style="top:176px"><svg width="16" height="16" viewBox="0 0 24 24"><path fill="#f7941d" d="M6.6 10.8c1.4 2.8 3.8 5.1 6.6 6.6l2.2-2.2c.3-.3.7-.4 1-.2 1.1.4 2.3.6 3.6.6.6 0 1 .4 1 1V20c0 .6-.4 1-1 1C10.6 21 3 13.4 3 4c0-.6.4-1 1-1h3.5c.6 0 1 .4 1 1 0 1.3.2 2.5.6 3.6.1.3 0 .7-.2 1z"/></svg><span>800-555-0142</span></div>
  <div class="contact" style="top:216px"><svg width="18" height="14" viewBox="0 0 18 14"><rect x="1" y="1" width="16" height="12" fill="none" stroke="#f7941d" stroke-width="2"/><path d="M1 1l8 7 8-7" fill="none" stroke="#f7941d" stroke-width="2"/></svg><span>support@valtrixenergy.example</span></div>
</footer>
<span class="social" style="left:176px"></span>
<span class="social" style="left:222px"></span>
<span class="social" style="left:270px"></span>
<div class="copyright">©VALTRIX ENERGY INFORMATION - 2018 All Right Reserved.</div>

</body>
</html>
```